High-End Medical Center Website Design Project

This design is part of a well thought-out project by an experienced project manager / developer. The approved wireframe is attached. Creative interpretations / suggestions based on the layout encouraged.

The design is for a new state-of-the-art medical center located in Dallas, Texas. The target audience would likely be individuals (approx. 60% female /40% male) who are the healthcare decision-makers for their families. They would likely have insurance and be inclined to seek out top-quality care.

Potential clients would choose this client over others in their industry because the medical center is physician owned, meaning it is patient-focused rather than profit-focused. The facility is brand new, featuring the latest technology. (This includes an amazing waiting room featuring WiFi and docking stations.) The physicians are hand-picked by referral only.

The look of the site should be extremely clean. We are going for a well-organized, professional look with a bit of a warm glow (interpret that however you like). Use crisp corners and the colors in the logo.

Think modern, clean with some great use of color / font.

We can get lovely photography of the medical center once construction is complete. Feel free to use an "example image" behind the Featured Area ("Physician Owned. Patient-Focused") if you like. We are open to ideas.

ONE CHANGE REQUESTED IN THE WIREFRAME:

Remove the "Connect" 1/4 page footer area and replace with a quick contact form. You may swap the "Locations" area with the form if desired. Put social media icons at the top left of the page in the top header area.

(Note: Please use social media icons that match the design rather than standard icons. We preferred not placing the icons at the top, but the client requested this. Let's not bring more attention to them than necessary.)
Updates

We're custom programming this site, so there's no need to base it on a template. Also, we would prefer not to use typical "seen everywhere" stock images.Thanks.

Industry/Entity Type

Construction

Requirements
Must have
• Follow the wireframe. This has been approved.
Nice to have
• Examples of what hover states, links or dropdowns might look like.

```html
<!DOCTYPE html>
<html lang="en">
<head>
<meta charset="utf-8">
<title>Nova Medical Center</title>
<link rel="stylesheet" href="https://fonts.googleapis.com/css2?family=Roboto+Condensed:wght@400;700&family=Open+Sans:ital,wght@0,400;0,600;1,600&display=swap">
<style>
:root{
  --blue:#0b52a3;
  --blue-dark:#08407f;
  --teal:#2a8fa3;
  --ink:#1b1b1b;
  --text:#4a4a4a;
  --muted:#6b6b6b;
  --topbar:#d8d8d8;
  --header:#e7e7e7;
  --panel:#ebebeb;
  --line:#d6d6d6;
  --white:#ffffff;
  --social:#9c9c9c;
}
*{box-sizing:border-box;margin:0;padding:0}
html,body{width:819px;height:1200px;overflow:hidden;background:var(--white)}
body{position:relative;font-family:"Open Sans",Arial,sans-serif;color:var(--text)}
.abs{position:absolute}
.cond{font-family:"Roboto Condensed","Arial Narrow",sans-serif}

/* top bar */
.topbar{left:0;top:0;width:819px;height:40px;background:var(--topbar)}
.social{left:15px;top:6px;display:flex;gap:5px}
.social span{width:26px;height:26px;background:var(--social);display:block}
.social span:first-child{background:var(--blue)}
.call{right:18px;top:8px;font-size:20px;color:var(--teal)}
.call b{font-weight:400;color:var(--blue)}

/* header */
.header{left:0;top:40px;width:819px;height:58px;background:var(--header)}
.brand{left:15px;top:60px;display:flex;align-items:center;gap:8px;font-size:25px;font-weight:700;color:var(--blue);letter-spacing:.5px}
.brand i{width:14px;height:14px;background:var(--blue);display:block}
.nav{left:328px;top:68px;display:flex;gap:10px}
.nav a{display:block;height:38px;padding:11px 11px 0;background:linear-gradient(#fafafa,#e3e3e3);border:1px solid #cfcfcf;border-bottom:none;font-size:14px;color:#555;text-decoration:none}
.nav a.active{color:var(--blue)}
.nav a:hover{color:var(--blue);background:#fff}

/* hero */
.hero{left:0;top:98px;width:819px;height:366px;background:linear-gradient(#f0f0f0,#f7f7f7)}
.hero-photo{left:250px;top:98px;width:569px;height:366px;background:linear-gradient(100deg,#eef0f2 0%,#dbe4ee 30%,#c9d8e8 55%,#d8dfe2 80%,#e9e3dc 100%)}
.hero-title{left:17px;top:186px;font-size:40px;line-height:40px;font-weight:700;color:var(--blue)}
.hero-sub{left:22px;top:280px;font-family:Arial,sans-serif;font-size:18px;line-height:20px;color:var(--ink)}
.stars{left:22px;top:360px;display:flex;gap:6px}
.hero-shadow{left:0;top:463px;width:819px;height:28px;background:radial-gradient(ellipse at 50% 0,rgba(0,0,0,.18),rgba(0,0,0,0) 70%)}
.badge{top:425px;width:82px;height:82px;border-radius:50%;background:var(--blue);border:3px solid var(--white);box-shadow:0 2px 5px rgba(0,0,0,.35);display:flex;align-items:center;justify-content:center}

/* features */
.features{left:15px;top:520px;width:788px;height:186px;border:1px solid #e2e2e2;border-radius:4px;background:var(--white)}
.sets{left:15px;top:520px;width:150px;height:186px}
.sets-label{left:32px;top:576px;font-size:24px;line-height:32px;color:var(--blue);font-weight:700;text-align:center;width:94px}
.feature{top:544px;width:160px}
.feature h3{font-family:"Roboto Condensed",sans-serif;font-weight:400;font-size:19px;color:#333;margin-bottom:6px}
.feature p{font-size:10.5px;line-height:17.4px;text-align:justify;color:var(--text)}
.divider{top:548px;width:1px;height:116px;background:#e4e4e4}

/* middle */
.portrait{left:17px;top:735px;width:168px;height:165px;border:1px solid #cfcfcf;border-radius:4px;padding:4px;background:var(--white);box-shadow:0 1px 4px rgba(0,0,0,.2)}
.portrait div{width:100%;height:100%;background:linear-gradient(135deg,#dde6ee,#9fc2e3 55%,#3f86c8)}
.intro{left:208px;top:738px;width:353px}
.intro h2,.testimonials h2{font-family:"Roboto Condensed",sans-serif;font-weight:400;font-size:20px;color:var(--blue)}
.intro p{margin-top:14px;font-size:10.5px;line-height:17.4px;text-align:justify}
.read{left:208px;top:874px;font-size:9.5px;font-style:italic;font-weight:600;color:var(--blue);text-decoration:none}
.testimonials{left:626px;top:731px;width:178px}
.testimonials p{font-size:10.5px;line-height:17.4px;text-align:justify}
.quote-first{margin:14px 0 0 33px}
.customer{display:block;margin-top:9px;font-size:9.5px;font-style:italic;font-weight:600;color:var(--blue)}

/* footer */
.footer{left:0;top:935px;width:819px;height:225px;background:var(--panel)}
.col{top:935px;height:225px;width:164px;border-right:1px solid var(--line)}
.col-head{position:absolute;left:15px;top:22px;display:flex;align-items:center;gap:8px;font-family:"Roboto Condensed",sans-serif;font-size:15px;color:var(--blue)}
.ic{width:30px;height:30px;border-radius:50%;background:var(--blue);display:flex;align-items:center;justify-content:center}
.list{position:absolute;left:18px;top:62px;width:120px;font-size:9.5px;line-height:13px;color:#333}
.list li{list-style:none;height:43.5px;background:radial-gradient(ellipse at 40% 100%,rgba(0,0,0,.12),rgba(0,0,0,0) 60%) no-repeat 0 34px/110px 8px}
.list li.first{color:var(--blue)}
.more{position:absolute;left:15px;top:177px;width:124px;height:20px;border-bottom:1px solid var(--blue)}
.more span{position:absolute;right:0;top:0;width:20px;height:20px;background:var(--blue);display:flex;align-items:center;justify-content:center}
.form{position:absolute;left:18px;top:63px;width:120px}
.field{height:22px;border:1px solid #cfcfcf;background:#f6f6f6;font-size:9px;font-style:italic;color:#555;padding:4px 6px;margin-bottom:7px}
.field.area{height:46px}
.submit{width:64px;height:20px;background:var(--blue);color:#fff;font-size:10px;font-weight:600;font-style:italic;border:none;display:block}
.loc{position:absolute;left:18px;top:63px;width:132px;font-size:9.5px;line-height:14px;color:#333}
.loc-row{display:flex;align-items:center;gap:12px;position:absolute;left:18px;font-size:9.5px;color:#333}
.wait{position:absolute;left:20px;width:130px}
.wait-head{display:flex;align-items:center;gap:8px;font-family:"Roboto Condensed",sans-serif;font-size:14px;color:var(--blue)}
.wait-head b{display:inline-block;width:22px;height:17px;background:var(--blue);color:#fff;font-size:12px;text-align:center;line-height:17px}
.wait p{font-size:9.5px;line-height:13px;color:#333;margin-top:3px}

/* bottom */
.bottom{left:0;top:1160px;width:819px;height:40px;background:#d0d0d0;font-size:9.5px}
.copy{left:15px;top:13px;color:#555}
.legal{right:17px;top:12px;color:#777}
.legal a{color:var(--blue);text-decoration:none}
.legal a:hover{text-decoration:underline}
</style>
</head>
<body>

<div class="abs topbar"></div>
<div class="abs social" aria-label="Social links"><span></span><span></span><span></span><span></span><span></span></div>
<div class="abs call cond">Call Now : <b>555-014-2290</b></div>

<div class="abs header"></div>
<div class="abs brand cond"><i></i>NOVA MEDICAL CENTER</div>
<nav class="abs nav cond">
  <a class="active" href="#">Why Nova</a>
  <a href="#">Phycisians</a>
  <a href="#">Specialities</a>
  <a href="#">Info</a>
  <a href="#">Locations</a>
  <a href="#">Contact Us</a>
</nav>

<section>
  <div class="abs hero"></div>
  <div class="abs hero-photo" role="img" aria-label="Photo of a physician examining a patient with a nurse beside them"></div>
  <h1 class="abs hero-title cond">Lorem ipsum<br>dolor</h1>
  <p class="abs hero-sub">Consectetur adipiscing elit.<br>Aliquam malesuada augue<br>eget mattis ultricies.</p>
  <div class="abs stars">
    <svg width="18" height="17" viewBox="0 0 24 23"><path d="M12 0l3.5 7.5 8.5 1-6.3 5.8 1.7 8.7L12 18.7 4.6 23l1.7-8.7L0 8.5l8.5-1z" fill="#0b52a3"/></svg>
    <svg width="18" height="17" viewBox="0 0 24 23"><path d="M12 0l3.5 7.5 8.5 1-6.3 5.8 1.7 8.7L12 18.7 4.6 23l1.7-8.7L0 8.5l8.5-1z" fill="#b5b5b5"/></svg>
    <svg width="18" height="17" viewBox="0 0 24 23"><path d="M12 0l3.5 7.5 8.5 1-6.3 5.8 1.7 8.7L12 18.7 4.6 23l1.7-8.7L0 8.5l8.5-1z" fill="#b5b5b5"/></svg>
    <svg width="18" height="17" viewBox="0 0 24 23"><path d="M12 0l3.5 7.5 8.5 1-6.3 5.8 1.7 8.7L12 18.7 4.6 23l1.7-8.7L0 8.5l8.5-1z" fill="#b5b5b5"/></svg>
    <svg width="18" height="17" viewBox="0 0 24 23"><path d="M12 0l3.5 7.5 8.5 1-6.3 5.8 1.7 8.7L12 18.7 4.6 23l1.7-8.7L0 8.5l8.5-1z" fill="#b5b5b5"/></svg>
  </div>
  <div class="abs hero-shadow"></div>
  <div class="abs badge" style="left:190px">
    <svg width="44" height="44" viewBox="0 0 44 44" fill="none" stroke="#fff" stroke-width="3" stroke-linecap="round"><path d="M8 6v10a8 8 0 0 0 16 0V6"/><path d="M16 24v6a8 8 0 0 0 16 0v-4"/><circle cx="32" cy="22" r="4"/></svg>
  </div>
  <div class="abs badge" style="left:409px">
    <svg width="44" height="40" viewBox="0 0 44 40" fill="#fff"><path d="M2 4h26v16H12l-6 5v-5H2z"/><path d="M31 10h11v16h-4v5l-6-5H16v-3h15z"/></svg>
  </div>
  <div class="abs badge" style="left:628px">
    <span class="cond" style="color:#fff;font-size:46px;font-weight:700">?</span>
  </div>
</section>

<section>
  <div class="abs features"></div>
  <svg class="abs sets" viewBox="0 0 150 186"><path d="M80 0l70 86-70 100" fill="none" stroke="#e0e0e0" stroke-width="2"/><path d="M78 4l66 82-66 96" fill="#fafafa"/></svg>
  <h2 class="abs sets-label cond">What sets us a part</h2>
  <div class="abs feature" style="left:190px"><h3>Technology</h3><p>Lorem ipsum dolor sit amet, consectetur adipiscing elit. Aliquam malesuada augue eget mattis ultricies. Maecenas felis sem, pretium quis venenatis quis, sodales nec</p></div>
  <div class="abs divider" style="left:379px"></div>
  <div class="abs feature" style="left:409px"><h3>Quality of care</h3><p>Lorem ipsum dolor sit amet, consectetur adipiscing elit. Aliquam malesuada augue eget mattis ultricies. Maecenas felis sem, pretium quis venenatis quis, sodales nec</p></div>
  <div class="abs divider" style="left:598px"></div>
  <div class="abs feature" style="left:628px"><h3>Patient Exprience</h3><p>Lorem ipsum dolor sit amet, consectetur adipiscing elit. Aliquam malesuada augue eget mattis ultricies. Maecenas felis sem, pretium quis venenatis quis, sodales nec</p></div>
</section>

<section>
  <div class="abs portrait"><div role="img" aria-label="Photo of a smiling nurse holding a tablet"></div></div>
  <div class="abs intro">
    <h2>Lorem ipsum dolor sit</h2>
    <p>Lorem ipsum dolor sit amet, consectetur adipiscing elit. Aliquam malesuada augue eget mattis ultricies. Maecenas felis sem, pretium quis venenatis quis, sodales nec dolor. Sed eu facilisis metus, non consectetur arcu. Nam in fermentum arcu, iaculis condimentum orci. Suspendisse consequat, diam vel lobortis pulvinar, odio lacus dapibus erat, sed sollicitudin</p>
  </div>
  <a class="abs read" href="#">Read more....</a>
  <div class="abs testimonials">
    <h2>Our Testimonials</h2>
    <svg class="abs" style="left:0;top:48px" width="23" height="18" viewBox="0 0 44 40" fill="#0b52a3"><path d="M2 4h26v16H12l-6 5v-5H2z"/><path d="M31 10h11v16h-4v5l-6-5H16v-3h15z"/></svg>
    <p class="quote-first">Lorem ipsum dolor sit amet, consectetur adipiscing elit. Integer molestie quam a</p>
    <p>Lorem ipsum dolor sit amet, consectetur adipiscing elit. Integer molestie quam a magna iaculis</p>
    <span class="customer">Customer Name</span>
  </div>
</section>

<footer>
  <div class="abs footer"></div>

  <div class="abs col" style="left:0">
    <div class="col-head"><span class="ic"><svg width="16" height="14" viewBox="0 0 16 14" fill="none" stroke="#fff" stroke-width="1.5"><rect x="1" y="1" width="14" height="12"/><path d="M4 5h8M4 8h8M4 11h5"/></svg></span>Recent News</div>
    <ul class="list"><li class="first">Lorem ipsum lorem&nbsp; ipsua dolor lorem</li><li>Lorem ipsum lorem&nbsp; ipsua dolor lorem</li><li>Lorem ipsum lorem&nbsp; ipsua dolor lorem</li></ul>
    <div class="more"><span><svg width="12" height="12" viewBox="0 0 12 12" fill="none" stroke="#fff" stroke-width="1.6"><path d="M5 7l2-2M4 6L2 8a2 2 0 0 0 2 2l2-2M8 6l2-2a2 2 0 0 0-2-2L6 4"/></svg></span></div>
  </div>

  <div class="abs col" style="left:164px">
    <div class="col-head" style="left:16px"><span class="ic"><svg width="18" height="16" viewBox="0 0 44 40" fill="#fff"><path d="M2 4h26v16H12l-6 5v-5H2z"/><path d="M31 10h11v16h-4v5l-6-5H16v-3h15z"/></svg></span>Recent Blog</div>
    <ul class="list" style="left:16px"><li>Lorem ipsum lorem&nbsp; ipsua dolor lorem</li><li>Lorem ipsum lorem&nbsp; ipsua dolor lorem</li><li>Lorem ipsum lorem&nbsp; ipsua dolor lorem</li></ul>
    <div class="more" style="left:16px"><span><svg width="12" height="12" viewBox="0 0 12 12" fill="none" stroke="#fff" stroke-width="1.6"><path d="M5 7l2-2M4 6L2 8a2 2 0 0 0 2 2l2-2M8 6l2-2a2 2 0 0 0-2-2L6 4"/></svg></span></div>
  </div>

  <div class="abs col" style="left:324px;width:160px">
    <div class="col-head" style="left:19px"><span class="ic"><svg width="16" height="12" viewBox="0 0 16 12" fill="none" stroke="#fff" stroke-width="1.5"><rect x="1" y="1" width="14" height="10"/><path d="M1 1l7 6 7-6"/></svg></span>Conatct Us</div>
    <form class="form" style="left:20px">
      <div class="field">Name</div>
      <div class="field">Email</div>
      <div class="field area">Message</div>
      <button class="submit" type="button">Submit</button>
    </form>
  </div>

  <div class="abs col" style="left:484px">
    <div class="col-head" style="left:17px"><span class="ic"><svg width="14" height="16" viewBox="0 0 14 16" fill="#fff"><path d="M7 0a5 5 0 0 1 5 5c0 4-5 9-5 9S2 9 2 5a5 5 0 0 1 5-5z"/><circle cx="7" cy="5" r="2" fill="#0b52a3"/></svg></span>Location</div>
    <p class="loc">Lorem ipsum dolor sit amet, consectetur adipisc. 012345 ABCD 0000</p>
    <div class="loc-row" style="top:130px"><svg width="18" height="20" viewBox="0 0 18 20" fill="none" stroke="#0b52a3" stroke-width="1.6"><rect x="3" y="2" width="10" height="16" rx="1"/><path d="M6 15h4"/></svg>Call : 555-014-2290</div>
    <div class="loc-row" style="top:180px"><svg width="20" height="15" viewBox="0 0 16 12" fill="none" stroke="#0b52a3" stroke-width="1.5"><rect x="1" y="1" width="14" height="10"/><path d="M1 1l7 6 7-6"/></svg>info@novamedical.example</div>
  </div>

  <div class="abs col" style="left:648px;width:171px;border-right:none">
    <div class="col-head" style="left:18px"><span class="ic"><svg width="18" height="18" viewBox="0 0 18 18" fill="none" stroke="#fff" stroke-width="1.6"><circle cx="9" cy="9" r="7"/><path d="M9 5v4l3 2"/></svg></span>Average wait Time</div>
    <div class="wait" style="top:70px"><div class="wait-head"><b>30</b>Minit wait</div><p>Lorem ipsum dolor sit amet, consectetur adipiscing elit.</p></div>
    <div class="wait" style="top:132px"><div class="wait-head"><b>30</b>Minit wait</div><p>Lorem ipsum dolor sit amet, consectetur adipiscing elit.</p></div>
    <div class="more" style="left:18px;width:135px"><span><svg width="12" height="12" viewBox="0 0 12 12" fill="none" stroke="#fff" stroke-width="1.6"><path d="M5 7l2-2M4 6L2 8a2 2 0 0 0 2 2l2-2M8 6l2-2a2 2 0 0 0-2-2L6 4"/></svg></span></div>
  </div>

  <div class="abs bottom">
    <span class="abs copy">Copyright© 2013 Nova medical center</span>
    <span class="abs legal"><a href="#">Site map</a> &nbsp;/&nbsp; <a href="#" style="color:#444">Privacy policy</a></span>
  </div>
</footer>

</body>
</html>
```